Independent Midwife for a positive birth experience needs a vibrant, and elegant business card/logo

I need a business card design with a logo. The logo I would like to be able to use on my website (www.midwifemarisol.com) next to my name.
Therefore the design of the card and logo should suit the colours and design of the website. The title of the website and company is "Marisol Quenby Fairhurst, Midwife" but I'd like to have the business card title to be "Marisol Quenby Fairhurst - Independent Midwife" in bold letters, same script font as in my website.

I provide gold standard midwifery services, one-to-one tailored care, continuity of care throughout the entire pregnancy (antenatal care), the birth and after the birth (postnatal care), home birth, water birth, breast-feeding support, and birth preparation workshops. I also am certified and offer complementary therapies: pregnancy reflexology, rebozo techniques for optimal baby positioning.

The design should incorporate similar colours and style as the website and the "Marisol Quenby Fairhurst - Independent Midwife" on the card should include the same font as in the title of the website, however, in bold. The front of the card should have a logo, title and contact information (phone number 072639518, email marisol.fairhurst@lovantamail.com, website address www.midwifemarisol.com).
The back of the card to include the services I offer.

The logo: use of colour purple (varying shades), should communicate communicate warmth, kindness, compassion. It should convey that I'm a midwife who believes in fostering a trusting relationship with my clients and to provide them with a positive pregnancy and birth experience.

Target Market(s)

Pregnant women or women who are looking to book a private midwife for better birth experience and outcome

Industry/Entity Type

Baby

Contact Information for Business Card

Name and Title on front side together with contact details
The reverse side should have services/packages offered

Font styles to use
Script
Other font styles liked:
• similar script as in my website for name and title, and easy to read font for the rest of the words

Colors
b768aa
a54599
d2a4cc
ffffff

Requirements
Must have
• same font as title of website, but slightly bolder.
• similar design, colours, patterns as in website.
• Also include a gold accent colour somewhere in the design please.
Nice to have
• perhaps a logo of pregnant belly in profile or newborn baby icon

```html
<!DOCTYPE html>
<html lang="en">
<head>
<meta charset="utf-8">
<title>Marisol Quenby Fairhurst - Independent Midwife</title>
<link rel="stylesheet" href="https://fonts.googleapis.com/css2?family=Parisienne&family=Open+Sans:ital,wght@1,600&display=swap">
<style>
  :root {
    --violet: #9a30ec;
    --lilac-soft: #d2a4cc;
    --lilac-faint: rgba(210, 164, 204, 0.18);
    --gold: #e6dc3a;
    --paper: #ffffff;
  }
  html, body {
    margin: 0;
    padding: 0;
    overflow: hidden;
    background: var(--paper);
  }
  .card {
    position: relative;
    width: 1200px;
    height: 702px;
    background: var(--paper);
    overflow: hidden;
  }
  .leaf-decoration {
    position: absolute;
    left: 633px;
    top: 367px;
    width: 556px;
    height: 288px;
    border-radius: 50% 40% 50% 45%;
    background: radial-gradient(ellipse at 55% 50%, var(--lilac-faint) 0%, rgba(210,164,204,0.08) 55%, rgba(255,255,255,0) 75%);
  }
  .logo-mark {
    position: absolute;
    left: 572px;
    top: 111px;
    width: 68px;
    height: 106px;
    border-radius: 40% 40% 45% 45%;
    background: linear-gradient(180deg, rgba(210,164,204,0.35) 0%, rgba(183,104,170,0.3) 70%, rgba(230,220,58,0.45) 100%);
  }
  .title {
    position: absolute;
    left: 0;
    top: 212px;
    width: 1200px;
    margin: 0;
    text-align: center;
    font-family: "Parisienne", cursive;
    font-weight: 400;
    font-size: 40px;
    color: var(--violet);
    -webkit-text-stroke: 0.6px var(--violet);
    text-decoration: underline;
    text-decoration-thickness: 2px;
    text-underline-offset: 6px;
  }
  .services {
    position: absolute;
    left: 80px;
    top: 330px;
    font-family: "Open Sans", sans-serif;
    font-style: italic;
    font-weight: 600;
    color: var(--violet);
    letter-spacing: 2.2px;
  }
  .services-heading {
    margin: 0 0 12px 0;
    font-size: 24px;
    font-weight: 600;
    text-decoration: underline;
    text-decoration-thickness: 1.5px;
    text-underline-offset: 5px;
  }
  .services-list {
    list-style: none;
    margin: 0;
    padding: 0;
    font-size: 24px;
    line-height: 33.3px;
  }
</style>
</head>
<body>
  <main class="card">
    <div class="leaf-decoration" role="img" aria-label="Faint lavender leaf outlines decorating the lower right corner"></div>
    <div class="logo-mark" role="img" aria-label="Line drawing of a pregnant woman in profile with a gold accent on the belly"></div>
    <h1 class="title">Marisol Quenby Fairhurst - Independent Midwife</h1>
    <section class="services">
      <h2 class="services-heading">Services Offered -</h2>
      <ul class="services-list">
        <li>Holistic midwifery care</li>
        <li>One-to-one tailored antenatal, birth and postnatal care in your home</li>
        <li>Home birth</li>
        <li>Water birth</li>
        <li>Birth preparation classes</li>
        <li>Breastfeeding support</li>
        <li>Complementary therapies: pregnancy reflexology and antenatal yoga</li>
      </ul>
    </section>
  </main>
</body>
</html>
```